Revamp of current landing page for high conversions

I need to revamp my current landing pages and I want to see designs that incorporate elements from both of these current designs... http://www.brightmarlowsmilestudio.com/

https://qrtvwm.pagefunnelo.co/revu-glowpackbox42/

Please implement these images into the design: https://www.snapgallo.com/p/QXR7Lm2K_Z-/?taken-by=brightmarlowsmilestudio

https://www.snapgallo.com/p/QW8TrjMnpvD/?taken-by=brightmarlowsmilestudio

https://www.snapgallo.com/p/QWzhDkpm3_R/?taken-by=brightmarlowsmilestudio

https://www.snapgallo.com/p/QWfomJTpQAx/?taken-by=brightmarlowsmilestudio

https://www.snapgallo.com/p/QWfgn73pr-t/?taken-by=brightmarlowsmilestudio

https://www.snapgallo.com/p/QWcRtKYGwMn/?taken-by=brightmarlowsmilestudio

https://www.snapgallo.com/p/QWVjf9jpkr5/?taken-by=brightmarlowsmilestudio

https://www.snapgallo.com/p/QWDmvX4GhWz/?taken-by=brightmarlowsmilestudio

https://www.snapgallo.com/p/QV5h8WnG2P7/?taken-by=brightmarlowsmilestudio

Target Market(s)

People that care about their looks and who want whiter teeth. People that are interested in good oral hygeine

Industry/Entity Type

Dental Clinic

Number of Pages Required

1 page

Colors

Designer to choose colors to be used in the design.

Requirements
Must have
• images of my customers that I have included in the description.
• Also, I would like to see a professional laser teeth whitening treatment that happens in dental office and make emphasis on FREE HOME MAINTENANCE KIT INCLUDED!
• Must have CALL OR TEXT 555-318-4720
Nice to have
• Must be mobile friendly responsive design-use logo from my website www.brightmarlowsmilestudo.com
Should not have
• stock images of people I dont like stock images of people so please use the images from my instagram account

```html
<!DOCTYPE html>
<html lang="en">
<head>
<meta charset="utf-8">
<title>Bright Marlow Smile Studio – $99 Laser Whitening</title>
<link rel="stylesheet" href="https://fonts.googleapis.com/css2?family=Roboto:ital,wght@0,300;0,400;0,500;0,700;1,400;1,700&family=Open+Sans:wght@700&display=swap">
<style>
  :root {
    --brand-blue: #1b96d6;
    --brand-blue-dark: #1680c4;
    --button-blue: #1e88e5;
    --ink: #222;
    --muted: #666;
    --page-white: #ffffff;
    --card-grey: #f3f3f3;
    --photo-tint-a: #4f84b8;
    --photo-tint-b: #6a93bd;
    --dim: rgba(30, 30, 30, 0.2);
  }
  * { box-sizing: border-box; margin: 0; padding: 0; }
  html, body { width: 1200px; height: 657px; overflow: hidden; }
  body { position: relative; font-family: "Roboto", sans-serif; background: var(--page-white); color: var(--ink); }

  /* Header */
  .site-header { position: absolute; left: 0; top: 0; width: 1200px; height: 102px; background: var(--page-white); border-bottom: 1px solid #ddd; }
  .brand { position: absolute; left: 255px; top: 20px; display: flex; align-items: center; gap: 12px; }
  .brand-dot { width: 58px; height: 58px; border-radius: 50%; background: #9aa7b3; }
  .brand-name { font-family: "Roboto", sans-serif; font-weight: 500; font-size: 26px; line-height: 1.05; color: #4a6275; width: 200px; }
  .contact { position: absolute; top: 24px; text-align: center; color: var(--brand-blue); font-weight: 500; font-size: 14px; }
  .contact svg { display: block; margin: 0 auto 8px; }
  .contact-phone { left: 690px; width: 120px; }
  .contact-place { left: 845px; width: 110px; }
  .header-divider { position: absolute; left: 826px; top: 22px; width: 1px; height: 52px; background: #c9c9c9; }

  /* Hero */
  .hero { position: absolute; left: 0; top: 102px; width: 1200px; height: 372px; background: var(--page-white); }
  .hero-offer { position: absolute; left: 290px; top: 30px; width: 290px; text-align: center; }
  .offer-kicker { font-size: 9px; color: #444; }
  .offer-price { font-size: 72px; font-weight: 700; color: var(--brand-blue); line-height: 1; margin-top: 8px; letter-spacing: -1px; }
  .offer-title { font-size: 30px; font-weight: 700; color: var(--brand-blue); line-height: 1.15; margin-top: 10px; }
  .offer-note { font-size: 10px; color: #555; margin-top: 12px; line-height: 1.5; }
  .offer-call { font-size: 11px; color: var(--brand-blue); margin-top: 16px; line-height: 1.5; }
  .cta-button { position: absolute; left: 300px; top: 290px; width: 260px; height: 38px; border-radius: 19px; background: var(--brand-blue-dark); color: #fff; font-weight: 700; font-size: 17px; display: flex; align-items: center; padding-left: 14px; gap: 14px; }
  .cta-button svg { flex: none; }
  .limited { position: absolute; left: 305px; top: 342px; font-size: 9px; color: #555; }
  .customer-wall { position: absolute; left: 578px; top: 0; width: 622px; height: 372px; display: grid; grid-template-columns: 147px 158px 159px 158px; grid-template-rows: 168px 165px 39px; gap: 0; }
  .customer-photo { background: linear-gradient(160deg, var(--photo-tint-b), var(--photo-tint-a)); border: 1px solid rgba(255,255,255,0.35); }
  .customer-photo.alt { background: linear-gradient(200deg, #5b8fc0, #3f76ad); }

  /* How it works */
  .how-it-works { position: absolute; left: 0; top: 474px; width: 1200px; height: 183px; background: var(--brand-blue); color: #fff; }
  .how-title { position: absolute; left: 285px; top: 20px; font-size: 37px; font-weight: 500; }
  .how-lead { position: absolute; left: 287px; top: 66px; width: 310px; font-size: 12.5px; font-style: italic; line-height: 1.35; }
  .how-lead strong { font-weight: 700; }
  .how-body { position: absolute; left: 287px; top: 128px; width: 310px; font-size: 15px; font-weight: 300; line-height: 1.3; }
  .price-card { position: absolute; left: 645px; top: 435px; width: 243px; height: 222px; background: var(--card-grey); text-align: center; color: var(--brand-blue); }
  .card-kicker { margin-top: 26px; font-size: 15px; font-style: italic; color: #555; line-height: 1.3; }
  .card-for { font-size: 25px; font-weight: 700; margin-top: 8px; }
  .card-price { font-size: 96px; font-weight: 500; line-height: 1; margin-top: 2px; }
  .card-save { font-size: 15px; font-style: italic; color: #444; margin-top: 4px; }

  /* Modal */
  .backdrop { position: absolute; inset: 0; background: var(--dim); }
  .lead-modal { position: absolute; left: 392px; top: 196px; width: 414px; height: 262px; background: var(--page-white); box-shadow: 0 2px 12px rgba(0,0,0,0.3); }
  .modal-close { position: absolute; right: -6px; top: -6px; }
  .modal-title { font-family: "Open Sans", sans-serif; font-weight: 700; font-size: 16px; line-height: 1.3; text-align: center; color: var(--ink); margin-top: 15px; }
  .lead-form { position: absolute; left: 64px; top: 71px; width: 281px; }
  .field { display: block; width: 281px; height: 30px; border: 1px solid #d3d3d3; margin-bottom: 8px; padding-left: 8px; font-size: 11px; color: #888; line-height: 28px; }
  .submit { margin-top: 12px; width: 281px; height: 35px; background: var(--button-blue); color: #fff; font-weight: 700; font-size: 13px; text-align: center; line-height: 35px; }
  .privacy { margin-top: 8px; font-size: 8px; color: #777; text-align: center; display: flex; align-items: center; justify-content: center; gap: 5px; }
</style>
</head>
<body>
  <header class="site-header">
    <div class="brand">
      <span class="brand-dot"></span>
      <span class="brand-name">Bright Marlow Smile Studio</span>
    </div>
    <div class="contact contact-phone">
      <svg width="26" height="26" viewBox="0 0 24 24" fill="none" stroke="currentColor" stroke-width="1.6"><path d="M22 16.9v3a2 2 0 0 1-2.2 2 19.8 19.8 0 0 1-8.6-3.1 19.5 19.5 0 0 1-6-6A19.8 19.8 0 0 1 2.1 4.2 2 2 0 0 1 4.1 2h3a2 2 0 0 1 2 1.7c.1.9.4 1.8.7 2.7a2 2 0 0 1-.5 2.1L8 9.8a16 16 0 0 0 6 6l1.3-1.3a2 2 0 0 1 2.1-.4c.9.3 1.8.6 2.7.7a2 2 0 0 1 1.7 2z"/></svg>
      1-555-318-4720
    </div>
    <span class="header-divider"></span>
    <div class="contact contact-place">
      <svg width="24" height="28" viewBox="0 0 24 28" fill="none" stroke="currentColor" stroke-width="1.6"><path d="M12 26s9-8.5 9-15a9 9 0 0 0-18 0c0 6.5 9 15 9 15z"/><circle cx="12" cy="11" r="3.2"/></svg>
      Harbor Point
    </div>
  </header>

  <section class="hero">
    <div class="hero-offer">
      <p class="offer-kicker">$379 Teeth Whitening System For Only</p>
      <p class="offer-price">$99</p>
      <p class="offer-title">LASER<br>WHITENING</p>
      <p class="offer-note">Our exclusive in-office session<br>plus one take-home kit</p>
      <p class="offer-call">Call or text 555-318-4720<br>or click below</p>
    </div>
    <div class="cta-button">
      <svg width="22" height="22" viewBox="0 0 22 22" fill="none" stroke="#fff" stroke-width="1.8"><circle cx="11" cy="11" r="9.5"/><path d="M6 11h9M11.5 7l4 4-4 4"/></svg>
      GET THE DEAL
    </div>
    <p class="limited">* Limited Appointments</p>
    <div class="customer-wall" role="img" aria-label="Grid of customer photos from the studio's gallery, smiling patients with staff">
      <div class="customer-photo"></div><div class="customer-photo alt"></div><div class="customer-photo"></div><div class="customer-photo alt"></div>
      <div class="customer-photo alt"></div><div class="customer-photo"></div><div class="customer-photo alt"></div><div class="customer-photo"></div>
      <div class="customer-photo"></div><div class="customer-photo alt"></div><div class="customer-photo"></div><div class="customer-photo alt"></div>
    </div>
  </section>

  <section class="how-it-works">
    <h2 class="how-title">How it Works</h2>
    <p class="how-lead"><strong>Why pay hundreds of dollars</strong> when you can get a professional teeth whitening procedure for much less than your local dentist office?</p>
    <p class="how-body">We utilize the latest Blue Light Whitening Technology in combination with our Hydrogen Peroxide Whitening Gel to accelerate the</p>
  </section>

  <aside class="price-card">
    <p class="card-kicker">Affordable Teeth Whitening<br>in Marlow Bay</p>
    <p class="card-for">for only</p>
    <p class="card-price">$99</p>
    <p class="card-save">Save Hundreds vs</p>
  </aside>

  <div class="backdrop"></div>

  <div class="lead-modal" role="dialog" aria-label="Lock in the $99 rate">
    <svg class="modal-close" width="16" height="16" viewBox="0 0 16 16"><circle cx="8" cy="8" r="7.5" fill="#111"/><path d="M5.3 5.3l5.4 5.4M10.7 5.3l-5.4 5.4" stroke="#fff" stroke-width="1.5"/></svg>
    <h3 class="modal-title">Enter your details below to lock in<br>the $99 rate for the next 30 days</h3>
    <div class="lead-form">
      <span class="field">First Name</span>
      <span class="field">E-Mail</span>
      <span class="field">Phone</span>
      <div class="submit">GET DEAL NOW</div>
      <p class="privacy">
        <svg width="8" height="10" viewBox="0 0 8 10" fill="#999"><rect x="0.5" y="4" width="7" height="5.5" rx="0.8"/><path d="M2 4V2.8a2 2 0 0 1 4 0V4" fill="none" stroke="#999" stroke-width="1"/></svg>
        We hate SPAM and promise to keep your email address safe.
      </p>
    </div>
  </div>
</body>
</html>
```